Geschäftspapiere für Rechtsberatung
Zielgruppe
Rechtsberatung; Zielgruppe sind sowohl Privat- als auch Geschäftsleute
Die Einzelkanzlei von Marlene Kosswig (Näheres siehe www.kosswig-beispiel.de) wird zu einer Partnergesellschaft, der
Kosswig

```html
<!DOCTYPE html>
<html lang="de">
<head>
<meta charset="utf-8">
<title>Briefbogen Kosswig Brenning</title>
<link rel="stylesheet" href="https://fonts.googleapis.com/css2?family=Arimo:wght@400;700&display=swap">
<style>
  :root {
    --brand-red: #9b1915;
    --text-grey: #7a7a7a;
    --light-grey: #a3a3a3;
    --paper: #ffffff;
  }
  html, body {
    margin: 0;
    padding: 0;
    overflow: hidden;
    background: var(--paper);
  }
  .letterhead {
    position: relative;
    width: 848px;
    height: 1200px;
    overflow: hidden;
    background: var(--paper);
    font-family: "Arimo", Arial, sans-serif;
    color: var(--text-grey);
  }
  .brand {
    position: absolute;
    left: 66px;
    top: 36px;
    display: flex;
    align-items: center;
    gap: 14px;
  }
  .brand-square {
    width: 70px;
    height: 70px;
    background: var(--brand-red);
  }
  .brand-name {
    font-size: 19px;
    line-height: 25px;
    font-weight: 400;
    color: var(--text-grey);
  }
  .sender {
    position: absolute;
    left: 628px;
    top: 42px;
    font-size: 11px;
    line-height: 13.4px;
    font-style: normal;
  }
  .sender .office-type {
    font-size: 14px;
    margin: 0 0 6px -2px;
  }
  .sender .firm {
    font-size: 13px;
    line-height: 14px;
    color: var(--light-grey);
    margin-left: 2px;
  }
  .sender .legal-form {
    font-weight: 700;
    color: var(--light-grey);
    margin: 0 0 13px 2px;
  }
  .sender p { margin: 0 0 13.4px 2px; }
  .side-band {
    position: absolute;
    top: 490px;
    width: 57px;
    height: 398px;
    background: var(--brand-red);
  }
  .side-band.left { left: 12px; }
  .side-band.right { right: 12px; }
</style>
</head>
<body>
<main class="letterhead">
  <header class="brand">
    <div class="brand-square"></div>
    <div class="brand-name">Kosswig Brenning</div>
  </header>

  <address class="sender">
    <div class="office-type">Rechtsanwaltskanzlei</div>
    <div class="firm">KOSSWIG § BRENNING</div>
    <div class="legal-form">PartG mbB</div>
    <p>Dipl.-Juristin<br>Marlene Kosswig<br>Lindenweg 14<br>45131 Feldhausen</p>
    <p>Tel.&nbsp; 02310/41 52 600<br>Fax&nbsp;&nbsp; 0231 / 41 52 602<br>Mobil 0170 / 41 52 603<br>info@kosswig-beispiel.de<br>www.kosswig-beispiel.de</p>
    <p>Nordwert Bank<br>IBAN: DE00 1234 5678<br>9012 3456 78<br>BIC: NORWDEX 1234</p>
    <p>Unser Zeichen<br>Datum</p>
  </address>

  <div class="side-band left" aria-hidden="true"></div>
  <div class="side-band right" aria-hidden="true"></div>
</main>
</body>
</html>
```